Fleeing Marisol Bay website

A very basic website using the graphics provided. The site would give the user the ability to read a description of the book, read testimonials, About the author, Read chapter 1, link to vantoro, order direct via quidlet.

```html
<!DOCTYPE html>
<html lang="en">
<head>
<meta charset="utf-8">
<title>Fleeing Marisol Bay</title>
<link rel="stylesheet" href="https://fonts.googleapis.com/css2?family=Open+Sans:ital,wght@0,300;0,400;0,600;1,400&display=swap">
<style>
:root{
  --maroon-deep:#230a0c;
  --maroon:#3a1216;
  --gold:#e0a030;
  --amber:#b8720e;
  --ink:#222;
  --text:#555;
  --muted:#8a8a8a;
  --line:#e3e3e3;
  --white:#fff;
}
*{margin:0;padding:0;box-sizing:border-box}
html,body{width:1001px;height:1200px;overflow:hidden;background:var(--white)}
body{position:relative;font-family:"Open Sans",Arial,sans-serif;color:var(--text)}
.abs{position:absolute}

.site-header{left:0;top:0;width:1001px;height:88px;background:var(--maroon-deep)}
.brand{left:77px;top:31px;font-family:"Open Sans",Arial,sans-serif;font-weight:600;font-size:25px;line-height:30px;color:var(--white);letter-spacing:.5px}
.social{right:84px;top:43px;display:flex;gap:3px}
.social i{display:block;width:26px;height:26px;border-radius:50%;background:var(--white)}

.main-nav{left:0;top:88px;width:1001px;height:42px;background:linear-gradient(#561f24,#3d1418);border-top:1px solid #5e272b;border-bottom:1px solid #2a0c0e}
.main-nav ul{list-style:none;display:flex;position:absolute;left:85px;top:0;height:41px}
.main-nav li{height:41px;line-height:41px;padding:0 22px;color:var(--white);font-size:14.5px;border-left:1px solid #2a0c0e;box-shadow:inset 1px 0 0 #5e272b}
.main-nav li:first-child{border-left:none;box-shadow:none}

.hero{left:0;top:130px;width:1001px;height:385px;background:radial-gradient(ellipse at 30% 30%,#47151a 0%,#2e0c10 55%,#240a0c 100%)}
.hero-kicker{left:87px;top:76px;font-size:27px;line-height:32px;font-weight:300;color:var(--gold)}
.hero-title{left:86px;top:108px;font-size:44px;line-height:48px;font-weight:400;color:var(--white);letter-spacing:-.3px}
.hero-copy{left:88px;top:166px;width:370px;font-size:11px;line-height:18.5px;color:#9b8184}
.btn-read{left:88px;top:209px;width:146px;height:36px;border-radius:2px;background:linear-gradient(#f6a443,#e87917);color:var(--white);font-size:13.5px;line-height:36px;padding-left:17px}
.btn-read::after{content:"";position:absolute;right:27px;top:0;width:1px;height:36px;background:#c9600e}
.btn-read svg{position:absolute;right:8px;top:11px}
.slider-dots{left:91px;top:258px;display:flex;gap:3px}
.slider-dots i{width:11px;height:11px;border-radius:50%;background:var(--white)}
.book-cover{left:601px;top:27px;width:212px;height:325px;background:linear-gradient(#2a0e10 0%,#3e3f40 30%,#4b6a78 55%,#262222 80%,#170808 100%);box-shadow:0 0 12px rgba(0,0,0,.6)}

h2{font-weight:300}
.about-title{left:73px;top:555px;font-size:27px;color:var(--ink)}
.author-photo{left:72px;top:598px;width:117px;height:129px;background:linear-gradient(160deg,#8a7a6e,#5e4a3e 60%,#2a2424)}
.about-lead{left:202px;top:594px;font-size:14.5px;color:#444}
.about-body{left:202px;top:619px;width:410px;font-size:11px;line-height:18.5px;color:#666}

.desc-title{left:651px;top:564px;font-size:23px;color:var(--amber)}
.desc-lead{left:651px;top:599px;font-size:13px;color:#444}
.desc-body{left:651px;top:618px;width:285px;font-size:11px;line-height:18.5px;color:var(--muted)}
.desc-body p+p{margin-top:6px}
.learn-more{left:652px;top:719px;font-size:12px;color:#333;letter-spacing:.2px}

.divider{left:69px;top:767px;width:862px;height:1px;background:var(--line)}

.testi-title{left:67px;top:790px;font-size:23px;color:var(--ink)}
.testi-card{top:831px;width:266px;height:215px;border:1px solid #e6e6e6;border-radius:2px;background:linear-gradient(#fff 60%,#f2f2f2);text-align:center}
.testi-card .avatar{position:absolute;left:97px;top:16px;width:72px;height:72px;border-radius:50%;border:2px solid #fff;box-shadow:0 0 3px rgba(0,0,0,.35)}
.testi-card blockquote{position:absolute;left:14px;top:99px;width:238px;font-style:italic;font-size:11px;line-height:18.5px;color:#666}
.testi-card cite{position:absolute;left:0;top:176px;width:100%;font-style:normal;font-size:11.5px;color:#333}

.side-title{font-size:21px}
.side-copy{width:285px;font-size:11px;line-height:18.5px;color:#9a9a9a}
.btn{width:100px;height:29px;border-radius:2px;color:var(--white);font-size:11.5px;line-height:29px;text-align:center}
.order-title{left:654px;top:796px;color:var(--maroon)}
.order-copy{left:655px;top:826px}
.btn-order{left:656px;top:871px;background:linear-gradient(#5a1e24,#3a1015)}
.vantoro-title{left:656px;top:929px;color:var(--amber)}
.vantoro-copy{left:656px;top:958px}
.btn-vantoro{left:657px;top:1001px;background:linear-gradient(#cf8418,#9c5a08)}

.site-footer{left:0;top:1098px;width:1001px;height:102px;background:linear-gradient(#f3f3f3,#fff 30%);border-top:1px solid #e2e2e2}
.footer-nav{left:81px;top:26px;font-size:13.5px;color:#555;word-spacing:1px}
.footer-nav b{font-weight:400;margin:0 7px}
.copyright{left:81px;top:53px;font-size:11px;color:#555}
</style>
</head>
<body>

<header class="site-header abs">
  <div class="brand abs">FLEEING MARISOL BAY</div>
  <div class="social abs" aria-label="Social links"><i></i><i></i><i></i><i></i></div>
</header>

<nav class="main-nav abs">
  <ul>
    <li>HOME</li><li>ABOUT US</li><li>MY NEW BOOK</li><li>ORDER NOW</li><li>TESTIMONIALS</li><li>SUPPORT</li><li>CONTACT</li>
  </ul>
</nav>

<section class="hero abs">
  <div class="hero-kicker abs">Checkout My New Book</div>
  <h1 class="hero-title abs">Fleeing Marisol Bay</h1>
  <p class="hero-copy abs">Aliquam nec erat at purus cursus interdum Vestibulum ligula augue bibendum accumsan vestibulum ut commodo a mi Morbi ornare</p>
  <div class="btn-read abs">Read Chapter 1
    <svg width="10" height="14" viewBox="0 0 10 14"><path d="M2 1l6 6-6 6" fill="none" stroke="#fff" stroke-width="1.6"/></svg>
  </div>
  <div class="slider-dots abs"><i></i><i></i><i></i><i></i></div>
  <div class="book-cover abs" role="img" aria-label="Book cover: a silhouetted man behind prison bars looking out at a tropical beach"></div>
</section>

<h2 class="about-title abs">About the author</h2>
<div class="author-photo abs" role="img" aria-label="Portrait photo of the author"></div>
<div class="about-lead abs">Phasellus felis dolor scelerisque a tempus eget lobortis</div>
<div class="about-body abs">
  <p>sed luctus quis feugiat in pede Fusce tellus Sed metus augue convallis et vehicula ut pulvinar eu ante &nbsp;Integer orci tellus tristique vitae consequat nec porta vel lectus Nulla sit amet diam Duis non nuncv</p>
  <p>libero a tempus libero lectus feugiat felis Morbi diam mauris viverra in gravida eu mattis in ante Morbi eget arcu Morbi porta libero id ullamcorper nonummy nibh ligula pulvinar Maecenas at justo id velit placerat molestie</p>
</div>

<h2 class="desc-title abs">Description of the book</h2>
<div class="desc-lead abs">Phasellus felis dolor scelerisque</div>
<div class="desc-body abs">
  <p>libero a tempus libero lectus feugiat felis Morbi diam mauris viverra in gravida eu mattis in ante Morbi eget arcu Morbi porta libero id ullamcorper</p>
  <p>Nonummy nibh ligula pulvinar Maecenas at justo id velit placerat molestie</p>
</div>
<div class="learn-more abs">LEARN MORE <svg width="5" height="8" viewBox="0 0 5 8"><path d="M0 0l5 4-5 4z" fill="#333"/></svg></div>

<div class="divider abs"></div>

<h2 class="testi-title abs">Testimonials</h2>
<article class="testi-card abs" style="left:69px">
  <div class="avatar" role="img" aria-label="Reader photo" style="background:linear-gradient(#e8e4e0,#b89a86)"></div>
  <blockquote>Aliquam nec erat at purus cursus interdum Vestibulum ligula augue bibendum accumsan vestibulum ut commodo a mi Morbi ornare gravida elit Integer congue aug</blockquote>
  <cite>By Author Name</cite>
</article>
<article class="testi-card abs" style="left:342px">
  <div class="avatar" role="img" aria-label="Reader photo" style="background:linear-gradient(#d8c9a0,#6f86b0)"></div>
  <blockquote>Aliquam nec erat at purus cursus interdum Vestibulum ligula augue bibendum accumsan vestibulum ut commodo a mi Morbi ornare gravida elit Integer congue aug</blockquote>
  <cite>By Author Name</cite>
</article>

<h2 class="side-title order-title abs">Order Direct via quidlet</h2>
<p class="side-copy order-copy abs">Aliquam nec erat at purus cursus interdum Vestibulum ligula augue bibendum accumsan vestibulum</p>
<div class="btn btn-order abs">ORDER NOW</div>

<h2 class="side-title vantoro-title abs">Link to vantoro</h2>
<p class="side-copy vantoro-copy abs">Aliquam nec erat at purus cursus interdum Vestibulum ligula augue bibendum accumsan vestibulum</p>
<div class="btn btn-vantoro abs">CLICK HERE</div>

<footer class="site-footer abs">
  <div class="footer-nav abs">HOME<b>|</b>ABOUT US<b>|</b>MY NEW BOOK<b>|</b>ORDER NOW<b>|</b>TESTIMONIALS<b>|</b>SUPPORT<b>|</b>CONTACT</div>
  <div class="copyright abs">© 2014 Company Name. &nbsp;All right reserved</div>
</footer>

</body>
</html>
```